I need a website, primarily a landing page, for my company, Corvane Group. A sales training and cons

I need a web design/landing page for a new sales training and consulting company, corvane group. We perform "sales experiments" aimed at each individual or team, where we assist in helping them identify their strengths, through a series of "sales experiments" that we can tailor based on the individual and what they're trying to accomplish.

```html
<!DOCTYPE html>
<html lang="en">
<head>
<meta charset="utf-8">
<title>Corvane Group – Sales Training &amp; Consulting</title>
<link href="https://fonts.googleapis.com/css2?family=Montserrat:wght@400;500;600&display=swap" rel="stylesheet">
<style>
:root{
  --blue:#2a68a8;
  --blue-dark:#1f5a96;
  --grey-panel:#8a8c8f;
  --ink:#2c2c2c;
  --muted:#444;
  --light-bg:#f6f6f6;
  --footer:#2b2b2b;
  --footer-line:#444;
  --white:#fff;
}
*{margin:0;padding:0;box-sizing:border-box}
html,body{width:1200px;height:2514px;overflow:hidden;background:var(--white)}
body{position:relative;font-family:Arial,Helvetica,sans-serif;color:var(--ink)}
h1,h2,h3,h4,h5{font-weight:400}
.abs{position:absolute}
.topline{left:0;top:0;width:1200px;height:4px;background:var(--blue-dark)}
.brand{left:112px;top:40px;display:flex;align-items:center;gap:12px;font-family:'Montserrat',sans-serif;font-weight:600;font-size:24px;color:var(--blue)}
.brand-dot{width:40px;height:40px;border-radius:50%;background:var(--blue)}
.call{left:864px;top:22px;display:flex;align-items:center;gap:12px}
.call-icon{width:54px;height:54px;border-radius:50%;background:var(--blue-dark);display:flex;align-items:center;justify-content:center}
.call-text{font-family:'Montserrat',sans-serif;font-weight:500;font-size:16px;color:var(--blue-dark)}
.nav{top:101px;font-family:'Montserrat',sans-serif;font-weight:600;font-size:13px;color:#333;transform:translateX(-50%);white-space:nowrap}
.nav.active{color:var(--blue-dark)}
.hero{left:0;top:144px;width:1200px;height:560px;background:linear-gradient(180deg,#6f6a66 0%,#8b857e 45%,#a29a90 100%)}
.hero-title{left:0;top:318px;width:1200px;text-align:center;font-family:'Montserrat',sans-serif;font-weight:600;font-size:50px;color:var(--white)}
.hero-sub{left:0;top:390px;width:1200px;text-align:center;font-family:'Montserrat',sans-serif;font-weight:400;font-size:35px;color:var(--white)}
.btn-ghost{border:2px solid rgba(255,255,255,.85);color:var(--white);font-family:'Montserrat',sans-serif;font-weight:500;display:flex;align-items:center;justify-content:center}
.hero-btn{left:484px;top:471px;width:232px;height:54px;border-radius:27px;font-size:19px}
.features{left:112px;top:551px;width:976px;height:324px;border:5px solid var(--white);display:flex;box-shadow:0 2px 6px rgba(0,0,0,.15)}
.feature{flex:1;position:relative;color:var(--white)}
.feature.blue{background:var(--blue)}
.feature.grey{background:var(--grey-panel)}
.feature h3{position:absolute;top:56px;font-family:'Montserrat',sans-serif;font-weight:500;font-size:22px}
.feature p{position:absolute;top:98px;width:352px;font-size:12px;line-height:26px;text-align:justify}
.feature .btn-ghost{position:absolute;top:231px;width:132px;height:41px;font-size:15px;border-width:1.5px}
.feature-badge{left:548px;top:652px;width:104px;height:104px;border-radius:50%;background:var(--white);display:flex;align-items:center;justify-content:center}
.feature-badge span{width:40px;height:40px;border-radius:50%;background:var(--blue)}
.section-title{left:0;width:1200px;text-align:center;font-family:'Montserrat',sans-serif;font-weight:400;font-size:37px;color:#222}
.rule{left:559px;width:82px;height:3px;background:var(--blue-dark)}
.about-text{left:236px;top:1016px;width:728px;text-align:center;font-size:12px;line-height:29px;color:var(--muted)}
.btn-solid{background:var(--blue-dark);color:var(--white);font-family:'Montserrat',sans-serif;font-weight:500;display:flex;align-items:center;justify-content:center}
.cta{left:0;top:1213px;width:1200px;height:362px;background:linear-gradient(90deg,#5b5550 0%,#7b746d 50%,#5e5a57 100%)}
.cta-title{left:0;top:1330px;width:1200px;text-align:center;font-family:'Montserrat',sans-serif;font-weight:500;font-size:27px;color:var(--white)}
.cta-sub{left:0;top:1370px;width:1200px;text-align:center;font-family:'Montserrat',sans-serif;font-weight:500;font-size:25px;color:var(--white)}
.blog-bg{left:0;top:1575px;width:1200px;height:621px;background:var(--light-bg)}
.card{top:1694px;width:312px;height:446px;background:var(--white);box-shadow:0 1px 4px rgba(0,0,0,.18)}
.card-img{height:228px;background:linear-gradient(135deg,#dfe4ea,#b9c2cc)}
.card h4{margin-top:26px;text-align:center;font-family:'Montserrat',sans-serif;font-weight:500;font-size:15px;color:#333}
.card .date{margin-top:18px;display:flex;justify-content:center;align-items:center;gap:7px;font-family:'Montserrat',sans-serif;font-weight:500;font-size:14px;color:var(--blue-dark)}
.card p{margin:14px 12px 0;text-align:center;font-size:12.5px;line-height:26px;color:var(--muted)}
.footer{left:0;top:2196px;width:1200px;height:318px;background:var(--footer)}
.social{top:2223px;width:60px;height:60px;border-radius:50%;border:1.5px solid #bbb;display:flex;align-items:center;justify-content:center}
.hr{left:112px;width:976px;height:1px;background:var(--footer-line)}
.contact{top:2338px;display:flex;gap:16px;color:var(--white)}
.contact-icon{width:54px;height:54px;border-radius:50%;border:1.5px solid #ccc;display:flex;align-items:center;justify-content:center;flex:none}
.contact h5{font-family:'Montserrat',sans-serif;font-weight:500;font-size:19px;margin-top:4px}
.contact p{font-size:12.5px;line-height:22px;margin-top:2px}
.copy{left:0;top:2468px;width:1200px;text-align:center;font-size:12.5px;color:var(--white)}
</style>
</head>
<body>
<div class="abs topline"></div>

<header>
  <div class="abs brand"><span class="brand-dot"></span>Corvane Group</div>
  <div class="abs call">
    <div class="call-icon"><svg width="20" height="20" viewBox="0 0 24 24"><path fill="#fff" d="M6.6 10.8a15 15 0 0 0 6.6 6.6l2.2-2.2c.3-.3.7-.4 1-.2 1.1.4 2.3.6 3.6.6.6 0 1 .4 1 1V20c0 .6-.4 1-1 1A17 17 0 0 1 3 4c0-.6.4-1 1-1h3.5c.6 0 1 .4 1 1 0 1.3.2 2.5.6 3.6.1.3 0 .7-.2 1z"/></svg></div>
    <div class="call-text">CALL US : 000-555-0147</div>
  </div>
  <nav>
    <span class="abs nav active" style="left:620px">HOME</span>
    <span class="abs nav" style="left:724px">ABOUT US</span>
    <span class="abs nav" style="left:838px">SERVICES</span>
    <span class="abs nav" style="left:938px">NEWS</span>
    <span class="abs nav" style="left:1049px">CONTACT US</span>
  </nav>
</header>

<section>
  <div class="abs hero" role="img" aria-label="Photo of a business team meeting around a table"></div>
  <h1 class="abs hero-title">CORVANE GROUP</h1>
  <h2 class="abs hero-sub">NEW SALES TRAINING &amp; CONSULTING</h2>
  <div class="abs btn-ghost hero-btn">GET A QUOTE</div>
</section>

<section class="abs features">
  <div class="feature blue">
    <h3 style="left:32px">NEW SALES TRAINING</h3>
    <p style="left:38px">Sed ut perspiciatis unde omnis iste natus error sit voluptatem accus antium doloremque laudantium, totam rem aperiam, eaque ipsa quae ab illo inventore veritatis et quasi architecto beatae vitae sit aspernatur aut odit aut fugit, sed quia conse quuntur</p>
    <div class="btn-ghost" style="left:41px">LEARN MORE</div>
  </div>
  <div class="feature grey">
    <h3 style="left:82px">SALES EXPERIMENTS</h3>
    <p style="left:84px">Sed ut perspiciatis unde omnis iste natus error sit voluptatem accus antium doloremque laudantium, totam rem aperiam, eaque ipsa quae ab illo inventore veritatis et quasi architecto beatae vitae sit aspernatur aut odit aut fugit, sed quia consequuntur</p>
    <div class="btn-ghost" style="left:85px">LEARN MORE</div>
  </div>
</section>
<div class="abs feature-badge"><span></span></div>

<section>
  <h2 class="abs section-title" style="top:932px">About Corvane Group</h2>
  <div class="abs rule" style="top:992px"></div>
  <p class="abs about-text">Sed ut perspiciatis unde omnis iste natus error sit voluptatem accusantium doloremque laudantium, totam rem aperiam, eaque ipsa quae ab illo inventore veritatis et quasi architecto beatae vitae dicta sunt explicabo. Nemo enim ipsam voluptatem quia voluptas sit aspernatur aut odit aut fugit, sed quia consequuntur magni dolores eos qui ratione voluptatem sequi nesciunt.</p>
  <div class="abs btn-solid" style="left:528px;top:1130px;width:144px;height:42px;font-size:15px">READ MORE</div>
</section>

<section>
  <div class="abs cta" role="img" aria-label="Photo of two business people shaking hands"></div>
  <h2 class="abs cta-title">SED UT PERSPICIATIS UNDE OMNIS</h2>
  <p class="abs cta-sub">error sit voluptatem accusantium doloremque laudantium</p>
  <div class="abs btn-solid" style="left:515px;top:1423px;width:170px;height:49px;font-size:17px">READ MORE</div>
</section>

<section>
  <div class="abs blog-bg"></div>
  <h2 class="abs section-title" style="top:1602px">Latest Blog</h2>
  <div class="abs rule" style="top:1655px"></div>

  <article class="abs card" style="left:112px">
    <div class="card-img" role="img" aria-label="Photo of a team working in an office"></div>
    <h4>SED UT PERSPICIATIS UNDE OMNIS</h4>
    <div class="date"><svg width="13" height="13" viewBox="0 0 14 14"><rect x="1" y="2.5" width="12" height="10.5" rx="1" fill="none" stroke="#1f5a96" stroke-width="1.5"/><path d="M1 5.5h12M4 1v3M10 1v3" stroke="#1f5a96" stroke-width="1.5"/></svg>OCT 20, 2018</div>
    <p>Nemo enim ipsam voluptatem quia voluptas sit aspernatur aut odit aut fugit, sed quia consequuntur magni ratione voluptatem sequi nesciunt.</p>
  </article>
  <article class="abs card" style="left:444px">
    <div class="card-img" role="img" aria-label="Photo of a meeting around a conference table"></div>
    <h4>SED UT PERSPICIATIS UNDE OMNIS</h4>
    <div class="date"><svg width="13" height="13" viewBox="0 0 14 14"><rect x="1" y="2.5" width="12" height="10.5" rx="1" fill="none" stroke="#1f5a96" stroke-width="1.5"/><path d="M1 5.5h12M4 1v3M10 1v3" stroke="#1f5a96" stroke-width="1.5"/></svg>OCT 20, 2018</div>
    <p>Nemo enim ipsam voluptatem quia voluptas sit aspernatur aut odit aut fugit, sed quia consequuntur magni ratione voluptatem sequi nesciunt.</p>
  </article>
  <article class="abs card" style="left:776px">
    <div class="card-img" role="img" aria-label="Photo of a presenter at a flip chart with a team"></div>
    <h4>SED UT PERSPICIATIS UNDE OMNIS</h4>
    <div class="date"><svg width="13" height="13" viewBox="0 0 14 14"><rect x="1" y="2.5" width="12" height="10.5" rx="1" fill="none" stroke="#1f5a96" stroke-width="1.5"/><path d="M1 5.5h12M4 1v3M10 1v3" stroke="#1f5a96" stroke-width="1.5"/></svg>OCT 20, 2018</div>
    <p>Nemo enim ipsam voluptatem quia voluptas sit aspernatur aut odit aut fugit, sed quia consequuntur magni ratione voluptatem sequi nesciunt.</p>
  </article>
</section>

<footer>
  <div class="abs footer"></div>
  <div class="abs social" style="left:391px" aria-label="Share"><svg width="18" height="18" viewBox="0 0 18 18"><circle cx="4" cy="9" r="2.2" fill="#fff"/><circle cx="14" cy="3.5" r="2.2" fill="#fff"/><circle cx="14" cy="14.5" r="2.2" fill="#fff"/><path d="M4 9l10-5.5M4 9l10 5.5" stroke="#fff" stroke-width="1.4"/></svg></div>
  <div class="abs social" style="left:463px" aria-label="Website"><svg width="18" height="18" viewBox="0 0 18 18" fill="none" stroke="#fff" stroke-width="1.4"><circle cx="9" cy="9" r="7.5"/><ellipse cx="9" cy="9" rx="3.2" ry="7.5"/><path d="M1.5 9h15"/></svg></div>
  <div class="abs social" style="left:533px" aria-label="Chat"><svg width="18" height="16" viewBox="0 0 18 16"><path d="M2 2h14v9H7l-4 3v-3H2z" fill="none" stroke="#fff" stroke-width="1.4" stroke-linejoin="round"/></svg></div>
  <div class="abs social" style="left:605px" aria-label="Link"><svg width="18" height="18" viewBox="0 0 18 18" fill="none" stroke="#fff" stroke-width="1.6" stroke-linecap="round"><path d="M7.5 10.5l3-3"/><path d="M8 5l1.5-1.5a3 3 0 0 1 4.2 4.2L12.2 9.2"/><path d="M10 13l-1.5 1.5a3 3 0 0 1-4.2-4.2L5.8 8.8"/></svg></div>
  <div class="abs social" style="left:676px" aria-label="Updates"><svg width="16" height="18" viewBox="0 0 16 18"><path d="M8 2a5 5 0 0 0-5 5v4l-1.5 2.5h13L13 11V7a5 5 0 0 0-5-5z" fill="none" stroke="#fff" stroke-width="1.4" stroke-linejoin="round"/><path d="M6.3 15.5a1.8 1.8 0 0 0 3.4 0" fill="none" stroke="#fff" stroke-width="1.4"/></svg></div>
  <div class="abs social" style="left:749px" aria-label="Email"><svg width="18" height="14" viewBox="0 0 18 14"><rect x="1" y="1" width="16" height="12" fill="none" stroke="#fff" stroke-width="1.5"/><path d="M1 1l8 7 8-7" fill="none" stroke="#fff" stroke-width="1.5"/></svg></div>
  <div class="abs hr" style="top:2310px"></div>

  <div class="abs contact" style="left:137px">
    <div class="contact-icon"><svg width="14" height="20" viewBox="0 0 14 20"><path fill="#fff" d="M7 0a7 7 0 0 0-7 7c0 5 7 13 7 13s7-8 7-13a7 7 0 0 0-7-7zm0 9.5A2.5 2.5 0 1 1 7 4.5a2.5 2.5 0 0 1 0 5z"/></svg></div>
    <div><h5>Address :</h5><p># 256 Lorem Ipsum dummy Text<br>Lorem Ipsum</p></div>
  </div>
  <div class="abs contact" style="left:513px">
    <div class="contact-icon"><svg width="18" height="14" viewBox="0 0 18 14"><rect x="1" y="1" width="16" height="12" fill="none" stroke="#fff" stroke-width="1.5"/><path d="M1 1l8 7 8-7" fill="none" stroke="#fff" stroke-width="1.5"/></svg></div>
    <div><h5>Email</h5><p>info@corvanegroup.com</p></div>
  </div>
  <div class="abs contact" style="left:865px">
    <div class="contact-icon"><svg width="18" height="18" viewBox="0 0 24 24"><path fill="#fff" d="M6.6 10.8a15 15 0 0 0 6.6 6.6l2.2-2.2c.3-.3.7-.4 1-.2 1.1.4 2.3.6 3.6.6.6 0 1 .4 1 1V20c0 .6-.4 1-1 1A17 17 0 0 1 3 4c0-.6.4-1 1-1h3.5c.6 0 1 .4 1 1 0 1.3.2 2.5.6 3.6.1.3 0 .7-.2 1z"/></svg></div>
    <div><h5>Phone</h5><p>Mobile : (000)-555-0147</p></div>
  </div>
  <div class="abs hr" style="top:2435px"></div>
  <p class="abs copy">© Copyright-2018 Corvane Group.All rights reserved</p>
</footer>
</body>
</html>
```